Website for Private Psychologist

DO NOT CONTACT ME PRIVATELY

I am a Psychologist offering psychotherapy for individuals and couples, and clinical consultation and training and education for mental and medical health professionals and agencies.

I need a redesign of my website

5 Pages (content is attached for each page)
Home
Jungian Psychotherapy
Clinical Consultation & Professional Development
Curriculum Vitae & Publications
Practice Policies and Forms

Designs can be based on these style websites
https://velmorcare.info; https://brantomind.org/; https://dorelhaskettpsychotherapy.com/

Minimalist Layout: Clean and uncluttered layout with generous white space, allowing the content and visuals to stand out'

Keep a linear, uncluttered, professional design.

Please use only royalty free images and google fonts. Please provide links to any stock images used to verify license.

private individual or couples seeking psychotherapy

Psychotherapy

5+ page

• No search feature

```html
<!DOCTYPE html>
<html lang="en">
<head>
<meta charset="utf-8">
<title>Dorian Vasquell, Psy.D.</title>
<link rel="stylesheet" href="https://fonts.googleapis.com/css2?family=Poppins:wght@300;400;500;600;700&family=Carlito:wght@400;700&display=swap">
<style>
:root{
  --ink:#1b2340;
  --text:#222;
  --blue:#3a7aa8;
  --blue-dark:#2f6b97;
  --band:#e8e9ec;
  --soft:#f4f4f4;
  --footer:#2a2a2a;
  --white:#fff;
  --line:#dcdde1;
}
*{box-sizing:border-box;margin:0;padding:0}
html,body{width:1200px;height:3420px;overflow:hidden}
body{position:relative;background:var(--white);font-family:"Carlito",sans-serif;color:var(--text)}
.abs{position:absolute}
.heading{font-family:"Poppins",sans-serif}
.btn{position:absolute;background:var(--blue);color:var(--white);font-family:"Poppins",sans-serif;font-weight:600;font-size:15px;display:flex;align-items:center;justify-content:center}

/* header */
.site-header{left:0;top:0;width:1200px;height:89px;background:var(--white)}
.brand{left:97px;top:12px;font-family:"Poppins",sans-serif;font-weight:600;color:var(--ink);text-align:center;line-height:1.1}
.brand .first{font-size:30px;display:block}
.brand .rest{font-size:16px;display:block}
.main-nav{left:293px;top:35px;display:flex;gap:20px;font-family:"Poppins",sans-serif;font-size:12.4px;color:var(--ink)}

/* hero */
.hero{left:0;top:89px;width:1200px;height:561px;background:linear-gradient(180deg,#6d7078 0%,#55585f 45%,#45474d 100%)}
.hero-welcome{left:0;top:145px;width:1200px;text-align:center;color:var(--white);font-family:"Poppins",sans-serif;font-weight:300;font-size:48px}
.hero-name{left:0;top:215px;width:1200px;text-align:center;color:var(--white);font-family:"Poppins",sans-serif;font-weight:700;font-size:58px}
.hero .btn{left:535px;top:326px;width:130px;height:51px}
.dots{left:575px;top:511px;display:flex;gap:9px}
.dots span{width:12px;height:12px;border-radius:50%;background:var(--white)}
.dots span.on{background:var(--blue)}

/* about */
.portrait{left:192px;top:758px;width:289px;height:385px;background:linear-gradient(160deg,#b49a74,#5a4a3a 55%,#24221f)}
.about-title{left:641px;top:762px;font-size:34px;font-weight:600;color:var(--blue)}
.license{left:641px;top:820px;font-size:19px;font-family:"Poppins",sans-serif;font-weight:400;color:var(--text)}
.about-sub{left:643px;top:872px;font-size:24px;font-weight:500;color:#111}
.about-text{left:644px;top:920px;width:456px;font-size:16px;line-height:25.6px}
.about-call{left:644px;top:1074px;width:151px;height:50px}

/* specializations */
.specs{left:0;top:1245px;width:1200px;height:613px;background:var(--band)}
.section-title{width:1200px;left:0;text-align:center;font-family:"Poppins",sans-serif;font-weight:600;font-size:36px;color:var(--blue)}
.specs .section-title{top:78px}
.spec{width:340px;text-align:center}
.spec .photo{width:260px;height:260px;border-radius:50%;margin:0 auto}
.spec h3{font-family:"Poppins",sans-serif;font-weight:500;font-size:24px;line-height:41px;color:#222;margin-top:32px}
.arrow{top:280px}

/* cv */
.cv-title{left:97px;top:1968px;font-size:36px;font-weight:600;line-height:48px;color:var(--blue)}
.cv-text{left:100px;top:2086px;width:456px;font-size:16px;line-height:25.6px}
.cv-btn{left:101px;top:2297px;width:129px;height:50px}
.cv-frame{left:601px;top:1994px;width:484px;height:352px;background:var(--blue);border-radius:18px}
.cv-photo{left:617px;top:1979px;width:484px;height:351px;border-radius:18px;background:linear-gradient(120deg,#d9d3c6,#b8a98e 45%,#6b5846 80%,#3c3a3c)}

/* contact */
.contact{left:0;top:2466px;width:1200px;height:586px;background:var(--soft)}
.contact .section-title{top:70px}
.field{position:absolute;background:var(--white);border-radius:4px;font-size:16px;color:#8a8a8a;padding:0 27px;display:flex;align-items:center}
.field.area{align-items:flex-start;padding-top:16px}
.touch-title{left:729px;top:148px;font-size:29px;font-weight:600;color:#111}
.info{left:733px;display:flex;gap:18px;font-size:16px;line-height:26px;color:#222}
.info svg{flex:none;margin-top:5px}
.social{display:flex;gap:9px}
.social span{width:40px;height:40px;border-radius:50%;border:1.5px solid var(--blue)}
.social span.fill{background:var(--blue)}

/* footer */
.site-footer{left:0;top:3052px;width:1200px;height:368px;background:var(--footer);color:var(--white)}
.foot-brand{left:0;width:1200px;text-align:center;font-family:"Poppins",sans-serif;font-weight:600;line-height:1.2}
.foot-nav{left:0;top:182px;width:1200px;display:flex;justify-content:center;gap:23px;font-family:"Poppins",sans-serif;font-size:14px}
.foot-social{left:0;top:238px;width:1200px;display:flex;justify-content:center;gap:6px}
.foot-social span{width:37px;height:37px;border-radius:50%;border:1.5px solid var(--white)}
.copy{left:0;top:296px;width:1200px;text-align:center;font-family:"Poppins",sans-serif;font-size:14.5px}
</style>
</head>
<body>

<header class="abs site-header">
  <div class="abs brand"><span class="first">Dorian</span><span class="rest">Vasquell, Psy.D.</span></div>
  <nav class="abs main-nav">
    <span>Home</span><span>Jungian Psychotherapy</span><span>Clinical Consultation &amp; Professional Development</span><span>Curriculum Vitae &amp; Publications</span><span>Practice Policies &amp; Forms</span>
  </nav>
</header>

<section class="abs hero" role="img" aria-label="Waiting room with black chairs and a reception desk, darkened">
  <div class="abs hero-welcome">Welcome to</div>
  <h1 class="abs hero-name">Dorian Vasquell, Psy.D.</h1>
  <div class="btn">Get Started</div>
  <div class="abs dots"><span></span><span class="on"></span><span></span></div>
</section>

<section class="about">
  <div class="abs portrait" role="img" aria-label="Portrait photo of the psychologist"></div>
  <h2 class="abs heading about-title">Dorian Vasquell, Psy.D.</h2>
  <p class="abs license">California Licensed Psychologist PSY 48215</p>
  <h3 class="abs heading about-sub">Jungian Psychotherapy &amp; Consultation</h3>
  <p class="abs about-text">I am a California Licensed Psychologist with an office in the San Francisco Financial District offering psychotherapy for individuals and couples, and clinical consultation and training and education for mental and medical health professionals and agencies. All appointments are currently available via telehealth.</p>
  <div class="btn about-call">(415) 555-0192</div>
</section>

<section class="abs specs">
  <h2 class="abs section-title">Specializations</h2>
  <svg class="abs arrow" style="left:54px" width="22" height="36" viewBox="0 0 22 36"><path d="M18 3 4 18l14 15" fill="none" stroke="#3a7aa8" stroke-width="4" stroke-linecap="round"/></svg>
  <svg class="abs arrow" style="left:1125px" width="22" height="36" viewBox="0 0 22 36"><path d="M4 3l14 15L4 33" fill="none" stroke="#8d9096" stroke-width="3" stroke-linecap="round"/></svg>
  <div class="abs spec" style="left:62px;top:167px">
    <div class="photo" role="img" aria-label="Office corner with window, bookshelf and plants" style="background:linear-gradient(135deg,#c9c7c0,#7b6a58 60%,#3e3630)"></div>
    <h3>Psychotherapy for<br>individuals</h3>
  </div>
  <div class="abs spec" style="left:430px;top:167px">
    <div class="photo" role="img" aria-label="Bookcase and wooden desk in the office" style="background:linear-gradient(135deg,#e2ddd4,#8a6a48 55%,#3a2f28)"></div>
    <h3>Psychotherapy for<br>couples</h3>
  </div>
  <div class="abs spec" style="left:800px;top:167px">
    <div class="photo" role="img" aria-label="Two armchairs and a lamp in the consulting room" style="background:linear-gradient(160deg,#d8d3ca,#9a8468 55%,#2f2d2d)"></div>
    <h3>clinical consultation</h3>
  </div>
</section>

<section class="cv">
  <h2 class="abs heading cv-title">Curriculum Vitae &amp;<br>Publications</h2>
  <p class="abs cv-text">Lorem ipsum dolor sit amet, consectetur adipiscing elit, sed do eiusmod tempor incididunt ut labore et dolore magna aliqua. Ut enim ad minim veniam, quis nostrud exercitation ullamco laboris nisi ut aliquip ex ea commodo consequat. Duis aute irure dolor in reprehenderit in voluptate velit esse cillum dolore eu fugiat nulla pariatur. Excepteur sint occaecat cupidatat non proident, sunt in culpa qui officia deserunt mollit anim id est laborum.</p>
  <div class="btn cv-btn">Learn More</div>
  <div class="abs cv-frame"></div>
  <div class="abs cv-photo" role="img" aria-label="Wooden chair with cushion beside a small side table"></div>
</section>

<section class="abs contact">
  <h2 class="abs section-title">Contact us</h2>
  <div class="field" style="left:139px;top:154px;width:250px;height:50px">First Name</div>
  <div class="field" style="left:405px;top:154px;width:251px;height:50px">Late Name</div>
  <div class="field" style="left:139px;top:220px;width:250px;height:50px">Email</div>
  <div class="field" style="left:403px;top:220px;width:251px;height:50px">Phone</div>
  <div class="field area" style="left:139px;top:286px;width:515px;height:138px">Messages</div>
  <div class="btn" style="left:143px;top:456px;width:130px;height:50px">Learn More</div>

  <h3 class="abs heading touch-title">Get in Touch</h3>
  <div class="abs info" style="top:210px">
    <svg width="14" height="18" viewBox="0 0 14 18"><path d="M7 0a7 7 0 0 0-7 7c0 5 7 11 7 11s7-6 7-11a7 7 0 0 0-7-7z" fill="#3a7aa8"/><circle cx="7" cy="7" r="2.6" fill="#f4f4f4"/></svg>
    <span>12 Lorem ipsum dolor sit amet, consec-<br>tetur adipiscing elit</span>
  </div>
  <div class="abs info" style="top:286px">
    <svg width="16" height="16" viewBox="0 0 16 16"><path d="M3.5 0.5l2.6 3-1.5 2a9 9 0 0 0 5 5l2-1.5 3 2.6-1.6 2.8C7 15 1 9 0.8 2.1z" fill="#3a7aa8"/></svg>
    <span>(415) 555-0192</span>
  </div>
  <div class="abs info" style="top:332px">
    <svg width="17" height="13" viewBox="0 0 17 13"><rect width="17" height="13" rx="1.5" fill="#3a7aa8"/><path d="M1 1.5l7.5 6 7.5-6" fill="none" stroke="#f4f4f4" stroke-width="1.6"/></svg>
    <span>dvasquell@quietmail.net</span>
  </div>
  <div class="abs social" style="left:731px;top:387px" aria-label="Social links"><span class="fill"></span><span></span><span></span><span></span></div>
</section>

<footer class="abs site-footer">
  <div class="abs foot-brand" style="top:70px;font-size:40px">Dorian</div>
  <div class="abs foot-brand" style="top:122px;font-size:21px">Vasquell, Psy.D.</div>
  <nav class="abs foot-nav">
    <span>Home</span><span>Jungian Psychotherapy</span><span>Clinical Consultation &amp; Professional Development</span><span>Curriculum Vitae &amp; Publications</span><span>Practice Policies &amp; Forms</span>
  </nav>
  <div class="abs foot-social" aria-label="Social links"><span></span><span></span><span></span><span></span><span></span></div>
  <p class="abs copy">©Copyrights 2023 Dorian Vasquell, Psy.D. &nbsp;| &nbsp; All Rights Reserved</p>
</footer>

</body>
</html>
```